Yard sign

Looking for a yard sign. <br/>Something simple, name, number. <br/>Large text, readable from 50 feet away. <br/><br/>18 x 24 inches.

Target Market(s)

Potential homeowners thinking about going solar.

Colors

Designer to choose colors to be used in the design.

Requirements
Must have
• "WE'VE GONE SOLAR!"
Nice to have
• We are a solar company, we would like a design that compliments the homeowners decision that they went solar and encourages others to do the same.

```html
<!DOCTYPE html>
<html lang="en">
<head>
<meta charset="utf-8">
<title>Bright Acre Solar – Yard Sign Designs</title>
<link rel="stylesheet" href="https://fonts.googleapis.com/css2?family=Bebas+Neue&family=Montserrat:wght@400;800&display=swap">
<style>
  :root {
    --board-grey: #a3a3a3;
    --sun-orange: #f7931e;
    --deep-orange: #e5851f;
    --sun-yellow: #fdc82f;
    --ink: #262626;
    --night: #1b1b1b;
    --white: #ffffff;
  }
  html, body {
    margin: 0;
    padding: 0;
    width: 1200px;
    height: 848px;
    overflow: hidden;
    background: var(--board-grey);
  }
  .board {
    position: relative;
    width: 1200px;
    height: 848px;
    font-family: "Montserrat", sans-serif;
  }
  .sign { position: absolute; display: block; }
  .sign--portrait { left: 40px; top: 62px; width: 544px; height: 725px; }
  .sign--landscape { left: 617px; top: 379px; width: 543px; height: 408px; }
  .brand-lockup { position: absolute; left: 0; top: 0; width: 1200px; height: 300px; }
  .display { font-family: "Bebas Neue", sans-serif; }
  .heavy { font-family: "Montserrat", sans-serif; font-weight: 800; }
  .caption {
    position: absolute;
    margin: 0;
    color: var(--white);
    font-weight: 400;
    letter-spacing: 0.02em;
  }
  .caption--design { left: 640px; width: 470px; top: 282px; text-align: center; font-size: 25px; }
  .caption--portrait { left: 40px; top: 802px; font-size: 17px; }
  .caption--landscape { left: 624px; top: 802px; font-size: 17px; }
</style>
</head>
<body>
<main class="board">

  <!-- Brand lockup (white on board) -->
  <svg class="brand-lockup" viewBox="0 0 1200 300" aria-label="Bright Acre Solar brand lockup">
    <circle cx="705" cy="160" r="42" fill="var(--white)"/>
    <text class="heavy" x="765" y="201" font-size="112" textLength="288" lengthAdjust="spacingAndGlyphs" fill="var(--white)">BAS</text>
    <text class="heavy" x="765" y="230" font-size="24" textLength="283" lengthAdjust="spacingAndGlyphs" fill="var(--white)">BRIGHT ACRE SOLAR</text>
  </svg>
  <p class="caption caption--design">YARD SIGN_DESIGN</p>

  <!-- Portrait yard sign -->
  <svg class="sign sign--portrait" viewBox="0 0 544 725" aria-label="Portrait yard sign">
    <defs>
      <linearGradient id="header-glow" x1="0" x2="1" y1="0" y2="0">
        <stop offset="0" stop-color="var(--deep-orange)"/>
        <stop offset="0.5" stop-color="var(--sun-orange)"/>
        <stop offset="1" stop-color="var(--deep-orange)"/>
      </linearGradient>
      <linearGradient id="phone-band" x1="0" x2="1" y1="0" y2="0">
        <stop offset="0" stop-color="#111"/>
        <stop offset="0.5" stop-color="#2a2a2a"/>
        <stop offset="1" stop-color="#111"/>
      </linearGradient>
    </defs>
    <rect class="sign-frame" width="544" height="725" fill="var(--sun-yellow)"/>
    <rect class="sign-panel" x="10" y="10" width="524" height="705" fill="var(--white)"/>
    <path class="sign-header" d="M0 0 H544 V272 Q272 376 0 272 Z" fill="url(#header-glow)"/>
    <circle cx="100" cy="160" r="30" fill="var(--white)"/>
    <text class="heavy" x="145" y="208" font-size="128" textLength="333" lengthAdjust="spacingAndGlyphs" fill="var(--white)">BAS</text>
    <text class="heavy" x="150" y="238" font-size="24" textLength="323" lengthAdjust="spacingAndGlyphs" fill="var(--white)">BRIGHT ACRE SOLAR</text>

    <text class="display" x="272" y="450" text-anchor="middle" font-size="143" textLength="470" lengthAdjust="spacingAndGlyphs" fill="var(--ink)">WE'VE GONE</text>
    <text class="display" x="272" y="573" text-anchor="middle" font-size="146" textLength="300" lengthAdjust="spacingAndGlyphs" fill="var(--ink)">SOLAR!</text>

    <rect class="phone-band" x="10" y="602" width="524" height="113" fill="url(#phone-band)"/>
    <path class="phone-icon" d="M50 622 q-6-4-10 0 l-8 10 q-10 18 0 42 l8 12 q4 4 10 0 l4-4 q3-3 0-8 l-6-8 q-3-3-7-1 q-6-12 0-26 q4 2 7-1 l6-8 q3-5 0-8 Z" fill="var(--sun-yellow)"/>
    <text class="display" x="74" y="694" font-size="104" textLength="435" lengthAdjust="spacingAndGlyphs" fill="var(--white)">555-014-2030</text>
  </svg>
  <p class="caption caption--portrait">POTRAIT _YARD SIGN</p>

  <!-- Landscape yard sign -->
  <svg class="sign sign--landscape" viewBox="0 0 543 408" aria-label="Landscape yard sign">
    <defs>
      <linearGradient id="call-band" x1="0" x2="1" y1="0" y2="0">
        <stop offset="0" stop-color="#111"/>
        <stop offset="0.5" stop-color="#2a2a2a"/>
        <stop offset="1" stop-color="#111"/>
      </linearGradient>
    </defs>
    <rect class="sign-frame" width="543" height="408" fill="var(--sun-yellow)"/>
    <rect class="sign-panel" x="10" y="8" width="523" height="392" fill="var(--white)"/>
    <circle cx="160" cy="98" r="18" fill="var(--sun-yellow)"/>
    <text class="heavy" x="190" y="122" font-size="70" textLength="189" lengthAdjust="spacingAndGlyphs" fill="var(--sun-orange)">BAS</text>
    <text class="heavy" x="192" y="137" font-size="13" textLength="185" lengthAdjust="spacingAndGlyphs" fill="var(--sun-orange)">BRIGHT ACRE SOLAR</text>

    <text class="display" x="271" y="251" text-anchor="middle" font-size="101" textLength="459" lengthAdjust="spacingAndGlyphs" fill="var(--night)">BRIGHT ACRE SOLAR</text>

    <rect class="tagline-band" x="10" y="269" width="523" height="60" fill="var(--sun-orange)"/>
    <text class="heavy" x="271" y="312" text-anchor="middle" font-size="40" textLength="440" lengthAdjust="spacingAndGlyphs" fill="var(--white)">WE'VE GONE SOLAR!</text>

    <rect class="call-band" x="10" y="333" width="523" height="67" fill="url(#call-band)"/>
    <text class="heavy" x="23" y="387" font-size="56" textLength="145" lengthAdjust="spacingAndGlyphs" fill="var(--sun-yellow)">CALL:</text>
    <text class="heavy" x="190" y="387" font-size="56" textLength="332" lengthAdjust="spacingAndGlyphs" fill="var(--white)">555-014-2030</text>
  </svg>
  <p class="caption caption--landscape">LANDSCAPE _YARD SIGN</p>

</main>
</body>
</html>
```